Business Card Design

I need a business card design for my new business based on Long Island, NY also serving NYC called Pawfield Lodge. I have built a website with cardmint that can be looked at as a basis for the card. It is pawfieldlodge.example.

I board Labrador Retrievers in my home. Specialize in one breed. Cage free environment. Dogs have full run of home and fenced in property. Pawfield Lodge is a one-of-a-kind, high-quality dog-boarding provider serving specifically Labrador Retrievers. By working with a dog I am comfortable with, I am able to offer the best care for all pets that come through my door. I work with Lab owners in the Long Island/NYC area to provide an
in-home safe, reliable and fun environment for daycare and overnight stays.

I provide a unique boarding experience for Labrador Retrievers on Long Island. Your Lab should be well mannered, housebroken and good with other dogs. Provided your pet is well mannered and house trained, my boarding services allow dogs to experience a cage-free stay while having free roam of my home and property. This allows owners a unique alternative to a kennel, giving pets the chance to experience a home away from home rather than chain linked fences and cold concrete floors.
As a guest at Pawfield Lodge, your dog will get:

4-star kibble
Access to my in-ground pool
All-natural snack selection
Companionship of other retrievers including my two
Full run of entire home and fenced-in backyard
Photos AND videos posted to Chatterly so you can see your dog having fun while away
Toys, bones and affection

I think it is important to have a pic of the 3 colored labs below. Also the picture of my own personal labs ..the white one with the black puppy. Maybe some paw prints. If using any imagery that MUST look EXACTLY like labrador retriever no generic dogs. Thank you
Updates

The Back of the Card should have the following: The background should be one of the pictures I sent (white dog in pool or another pic I included) At Pawfield Lodge your Lab gets: Cage Free Environment Full run of my home and fenced in yard In-ground pool Toys and affection Companionship of other Labrador Retrievers Photos and Videos posted Chatterly of your loved one FRONT OF THE CARD: should include picture of the 3 labs (yellow white brown) OR picture of white dog in pool. Pawfield Lodge should be in larger font than the rest. the following can be in any order. Ned Holm Maplecrest, NY in Central Long Island pawfieldlodge.example 555-271-4096

Industry/Entity Type

Environment

Contact Information for Business Card

Pawfield Lodge
Maplecrest, NY
Ned Holm
pawfieldlodge@mailbox.example
555-271-4096

```html
<!DOCTYPE html>
<html lang="en">
<head>
<meta charset="utf-8">
<title>Pawfield Lodge – Business Card</title>
<link href="https://fonts.googleapis.com/css2?family=Open+Sans:wght@400;700&family=Roboto:wght@400;700&display=swap" rel="stylesheet">
<style>
  :root {
    --page: #ecebee;
    --pink: #ee7ba3;
    --pink-light: #f6b3ca;
    --teal: #2f9a86;
    --teal-soft: #5cc3ad;
    --gray-mid: #b9b3b8;
    --white: #ffffff;
    --ink: #141414;
    --photo-grass: #6f8f45;
    --photo-dog-dark: #3e2a22;
    --photo-dog-light: #e9dcc0;
    --photo-room: #c8902e;
    --photo-room-light: #efe2c6;
  }
  * { box-sizing: border-box; margin: 0; padding: 0; }
  html, body { width: 1200px; height: 800px; overflow: hidden; }
  body { background: var(--page); position: relative; }

  .card {
    position: absolute;
    top: 245px;
    width: 540px;
    height: 309px;
    overflow: hidden;
    box-shadow: 0 6px 18px rgba(0,0,0,.18);
    background: var(--white);
  }
  .card--back { left: 40px; }
  .card--front { left: 620px; }
  .card-art { position: absolute; inset: 0; width: 540px; height: 309px; }

  /* back of card */
  .back-title {
    position: absolute;
    right: 26px;
    top: 150px;
    font-family: "Open Sans", sans-serif;
    font-weight: 700;
    font-size: 24px;
    line-height: 1;
    color: var(--ink);
  }
  .perk-list {
    position: absolute;
    right: 26px;
    top: 182px;
    list-style: none;
    text-align: right;
    white-space: nowrap;
    font-family: "Open Sans", sans-serif;
    font-size: 11.5px;
    line-height: 15px;
    color: var(--teal);
  }

  /* front of card */
  .front-title {
    position: absolute;
    left: 30px;
    top: 30px;
    font-family: "Roboto", sans-serif;
    font-weight: 700;
    font-size: 36px;
    line-height: 1;
    color: var(--ink);
  }
  .contact {
    position: absolute;
    left: 40px;
    top: 92px;
    font-family: "Roboto", sans-serif;
    color: var(--ink);
  }
  .contact-name { font-weight: 700; font-size: 24px; line-height: 1.1; margin-bottom: 4px; }
  .contact-line { font-size: 14px; line-height: 21px; }
  .contact-line--strong { font-weight: 700; }
  .front-web {
    position: absolute;
    left: 30px;
    bottom: 26px;
    font-family: "Roboto", sans-serif;
    font-weight: 700;
    font-size: 16px;
    letter-spacing: .5px;
    color: var(--white);
    text-transform: uppercase;
  }
</style>
</head>
<body>

<section class="card card--back" aria-label="Back of business card">
  <svg class="card-art" viewBox="0 0 540 309">
    <defs>
      <linearGradient id="grassDogs" x1="0" y1="0" x2="1" y2="1">
        <stop offset="0" stop-color="var(--photo-grass)"/>
        <stop offset=".35" stop-color="var(--photo-dog-dark)"/>
        <stop offset=".6" stop-color="var(--photo-dog-light)"/>
        <stop offset=".85" stop-color="#1d1d1d"/>
        <stop offset="1" stop-color="var(--photo-grass)"/>
      </linearGradient>
    </defs>
    <rect class="band-pink" width="540" height="309" fill="var(--pink)"/>
    <path class="photo-three-labs" role="img" aria-label="Photo of three Labrador Retrievers, chocolate, yellow and black, lying on grass"
          d="M0,0 H420 V90 C390,92 365,105 352,122 C320,108 280,110 262,130 C220,118 180,120 160,130 H0 Z"
          fill="url(#grassDogs)"/>
    <path class="scallop-edge" d="M0,309 V205 C40,190 80,186 118,194 C150,168 210,166 242,176 C270,150 320,136 362,138 C395,126 445,122 474,128 C502,122 530,124 540,126 V309 Z"
          fill="var(--pink-light)"/>
    <path class="scallop-white" d="M0,309 V213 C40,198 80,194 118,202 C150,176 210,174 242,184 C270,158 320,144 362,146 C395,134 445,130 474,136 C502,130 530,132 540,134 V309 Z"
          fill="var(--white)"/>
  </svg>
  <h2 class="back-title">Pawfield Lodge</h2>
  <ul class="perk-list">
    <li>4-star kibble</li>
    <li>Access to my in-ground pool</li>
    <li>All-natural snack selection</li>
    <li>Companionship of other retrievers including my two</li>
    <li>Full run of entire home and fenced-in backyard</li>
    <li>Photos AND videos posted to Chatterly so you can see your dog having<br>fun while away</li>
    <li>Toys, bones and affection</li>
  </ul>
</section>

<section class="card card--front" aria-label="Front of business card">
  <svg class="card-art" viewBox="0 0 540 309">
    <defs>
      <linearGradient id="frontWash" x1="0" y1="0" x2="0" y2="1">
        <stop offset="0" stop-color="var(--teal-soft)"/>
        <stop offset=".4" stop-color="var(--gray-mid)"/>
        <stop offset=".75" stop-color="var(--pink-light)"/>
        <stop offset="1" stop-color="var(--pink)"/>
      </linearGradient>
      <linearGradient id="roomDogs" x1="0" y1="0" x2="0" y2="1">
        <stop offset="0" stop-color="var(--photo-room)"/>
        <stop offset=".45" stop-color="var(--photo-room-light)"/>
        <stop offset=".8" stop-color="#2a2a2a"/>
        <stop offset="1" stop-color="#d9d3c8"/>
      </linearGradient>
    </defs>
    <rect class="front-wash" width="540" height="309" fill="url(#frontWash)"/>
    <path class="photo-own-labs" role="img" aria-label="Photo of a white Labrador Retriever with a black Labrador puppy indoors"
          d="M540,58 H440 C380,66 350,118 350,182 C350,244 368,288 390,309 H540 Z"
          fill="url(#roomDogs)"/>
  </svg>
  <h1 class="front-title">Pawfield Lodge</h1>
  <div class="contact">
    <p class="contact-name">Ned Holm</p>
    <p class="contact-line">Maplecrest, NY</p>
    <p class="contact-line contact-line--strong">Email: pawfieldlodge@mailbox.example</p>
    <p class="contact-line contact-line--strong">Phone: 555-271-4096</p>
  </div>
  <p class="front-web">www.pawfieldlodge.example</p>
</section>

</body>
</html>
```